Lanternfield Voyages Business Card Design for Home Based Travel Agency

We already have a logo and I would like to see about getting a Business Card Design. The font on the logo can be changed. We are a home based travel agency and sell cruises and tour packages, etc. I would like the following information put into the design Name of Company and Tag Line from the logo. I would also like the email info@lanternfieldvoyages.example Phone 555-238-6140. Website www.lanternfieldvoyages.example. My name Neil Parton Travel Consultant and my wife's Name Mavis Parton. I would like you to use your imagination as nothing is off limites. Impress Me!

Target Market(s)

Baby Boomers

Industry/Entity Type

Travel Agent

Contact Information for Business Card

See above

Font styles to use
Serif
Sans Serif

Colors

Designer to choose colors to be used in the design.

Requirements
Must have
• Play with different fonts and needs to be easily readable, i.e. not too small of print.
Nice to have
• Use your imagination

```html
<!DOCTYPE html>
<html lang="en">
<head>
<meta charset="utf-8">
<title>Lanternfield Voyages Business Card</title>
<link rel="stylesheet" href="https://fonts.googleapis.com/css2?family=Open+Sans:wght@400;600;700&display=swap">
<style>
  :root {
    --backdrop: #e9e7e4;
    --card: #ffffff;
    --band: #474847;
    --ink: #2b2b2b;
    --ink-soft: #4a4a4a;
    --on-band: #ffffff;
    --accent: #f28a24;
    --rule: #dcdcdc;
  }
  * { box-sizing: border-box; margin: 0; padding: 0; }
  html, body {
    width: 1200px; height: 900px; overflow: hidden;
    background: var(--backdrop);
    font-family: "Open Sans", Arial, sans-serif;
  }
  .canvas { position: relative; width: 1200px; height: 900px; }
  .card {
    position: absolute; width: 600px; height: 360px;
    background: var(--card);
    box-shadow: 0 10px 30px rgba(0,0,0,.18);
    overflow: hidden;
  }
  .card--front { left: 90px; top: 50px; }
  .card--back { left: 510px; top: 490px; }

  /* front */
  .front-band {
    position: absolute; left: 0; top: 88px; width: 470px; height: 188px;
    background: var(--band); color: var(--on-band);
    padding: 22px 0 0 31px;
  }
  .names { font-weight: 600; font-size: 21px; letter-spacing: .1px; white-space: nowrap; }
  .role { font-size: 15px; margin-top: 4px; }
  .contact { list-style: none; margin-top: 34px; font-size: 15px; line-height: 21px; }
  .contact li { display: flex; align-items: center; gap: 8px; white-space: nowrap; }
  .contact svg { width: 12px; height: 12px; fill: var(--on-band); flex: none; }
  .front-brand {
    position: absolute; left: 470px; top: 88px; width: 130px; height: 188px;
    display: flex; flex-direction: column; align-items: center; justify-content: center; gap: 12px;
    text-align: center;
  }
  .brand-square { width: 44px; height: 44px; background: var(--accent); }
  .brand-name { font-weight: 600; font-size: 17px; line-height: 21px; color: var(--ink); }

  /* back */
  .back-band { position: absolute; left: 0; width: 100%; background: var(--band); }
  .back-band--top { top: 0; height: 36px; }
  .back-band--bottom { bottom: 0; height: 42px; }
  .back-panel {
    position: absolute; left: 74px; right: 74px; top: 36px; bottom: 42px;
    border-left: 1px solid var(--rule); border-right: 1px solid var(--rule);
    display: flex; flex-direction: column; align-items: center; justify-content: center;
    text-align: center;
  }
  .back-square { width: 70px; height: 70px; background: var(--accent); margin-bottom: 22px; }
  .back-name { font-weight: 600; font-size: 34px; color: var(--ink); letter-spacing: .5px; white-space: nowrap; }
  .tagline { font-size: 15px; color: var(--ink-soft); margin-top: 8px; white-space: nowrap; }
</style>
</head>
<body>
<div class="canvas">

  <section class="card card--front">
    <div class="front-band">
      <p class="names">Neil Parton | Mavis Parton</p>
      <p class="role">Travel Consultant</p>
      <ul class="contact">
        <li><svg viewBox="0 0 24 24" aria-hidden="true"><path d="M6.6 10.8a15 15 0 0 0 6.6 6.6l2.2-2.2a1 1 0 0 1 1-.25 11.4 11.4 0 0 0 3.6.57 1 1 0 0 1 1 1V20a1 1 0 0 1-1 1A17 17 0 0 1 3 4a1 1 0 0 1 1-1h3.5a1 1 0 0 1 1 1c0 1.25.2 2.45.57 3.57a1 1 0 0 1-.25 1z"/></svg>555-238-6140</li>
        <li><svg viewBox="0 0 24 24" aria-hidden="true"><path d="M2 5h20v14H2z M3.5 6.5 12 13l8.5-6.5" fill="none" stroke="#fff" stroke-width="2.4"/></svg>info@lanternfieldvoyages.example</li>
        <li><svg viewBox="0 0 24 24" aria-hidden="true"><circle cx="12" cy="12" r="10"/></svg>www.lanternfieldvoyages.example</li>
      </ul>
    </div>
    <div class="front-brand">
      <span class="brand-square"></span>
      <span class="brand-name">Lanternfield<br>Voyages</span>
    </div>
  </section>

  <section class="card card--back">
    <div class="back-band back-band--top"></div>
    <div class="back-panel">
      <span class="back-square"></span>
      <p class="back-name">Lanternfield Voyages</p>
      <p class="tagline">Every Journey Becomes a Tale to Tell</p>
    </div>
    <div class="back-band back-band--bottom"></div>
  </section>

</div>
</body>
</html>
```